Business Card Design for Occupational Medicine Start Up Company

We need to design a professional business card. We are a healthcare company providing occupational medicine services to blue collar industries. We are professional, efficient and high quality service providers.

Target Market(s)

Blue Collar Industry: Shipbuilding, Ports, Trucking Companies; The Executives and Safety Officers for these companies

Industry/Entity Type

Healthcare

Contact Information for Business Card

Logo, Name, Title, Email, Phone

Other font styles liked:
• Please match our Brand Guide

Requirements
Must have
• Our Company Colors and Logo

```html
<!DOCTYPE html>
<html lang="en">
<head>
<meta charset="utf-8">
<title>ShiftWell Clinics – Business Card</title>
<link rel="stylesheet" href="https://fonts.googleapis.com/css2?family=Montserrat:wght@600;700&family=Questrial&display=swap">
<style>
  :root {
    --stage: #2b2b2d;
    --sky: #29a7e1;
    --sky-deep: #1f96d3;
    --navy: #23367f;
    --amber: #f2a93b;
    --ink-grey: #6b6b6b;
    --paper: #ffffff;
  }
  * { box-sizing: border-box; margin: 0; padding: 0; }
  html, body {
    width: 1200px; height: 1024px; overflow: hidden;
    background: var(--stage);
  }
  .stage {
    width: 1200px; height: 1024px;
    display: flex; flex-direction: column; align-items: center; justify-content: center;
    gap: 56px;
  }
  .card {
    width: 640px; height: 366px; position: relative; overflow: hidden;
    box-shadow: 0 10px 30px rgba(0,0,0,.45);
  }

  /* Back side */
  .card-back {
    background: var(--sky);
  }
  .card-back .pattern {
    position: absolute; inset: 0;
    background: linear-gradient(135deg, var(--sky) 0%, var(--sky-deep) 100%);
  }
  .card-back .brand {
    position: absolute; left: 330px; top: 170px;
    display: flex; align-items: center; gap: 12px;
  }
  .card-back .brand-dot {
    width: 34px; height: 34px; border-radius: 50%; background: var(--paper);
  }
  .card-back .brand-name {
    font-family: "Montserrat", sans-serif; font-weight: 700;
    font-size: 22px; letter-spacing: 1px; text-transform: uppercase;
    color: var(--paper);
  }

  /* Front side */
  .card-front { background: var(--paper); }
  .card-front .brand {
    position: absolute; left: 40px; top: 0; bottom: 0; width: 230px;
    display: flex; flex-direction: column; align-items: center; justify-content: center; gap: 18px;
  }
  .card-front .brand-dot {
    width: 64px; height: 64px; border-radius: 50%; background: var(--navy);
  }
  .card-front .brand-name {
    font-family: "Montserrat", sans-serif; font-weight: 700;
    font-size: 23px; letter-spacing: 1px; text-transform: uppercase;
    color: var(--navy); text-align: center; line-height: 1.15;
  }
  .divider {
    position: absolute; left: 296px; top: 92px; width: 1px; height: 182px;
    background: var(--navy);
  }
  .person {
    position: absolute; left: 324px; top: 98px;
  }
  .person-name {
    font-family: "Montserrat", sans-serif; font-weight: 700;
    font-size: 27px; color: var(--navy); text-transform: uppercase; letter-spacing: .5px;
  }
  .person-title {
    font-family: "Questrial", sans-serif; font-size: 14px; color: var(--ink-grey);
    margin-top: 4px;
  }
  .contacts {
    list-style: none; margin-top: 22px;
    display: flex; flex-direction: column; gap: 9px;
  }
  .contacts li {
    display: flex; align-items: center; gap: 10px;
    font-family: "Questrial", sans-serif; font-size: 15px; color: var(--ink-grey);
  }
  .contacts .icon {
    width: 16px; height: 16px; border-radius: 50%; background: var(--amber);
    display: flex; align-items: center; justify-content: center; flex: none;
  }
  .contacts .icon svg { width: 10px; height: 10px; }
</style>
</head>
<body>
<main class="stage">

  <section class="card card-back" aria-label="Card back">
    <div class="pattern" role="img" aria-label="Repeating tone-on-tone pattern of the company mark on sky blue"></div>
    <div class="brand">
      <span class="brand-dot"></span>
      <span class="brand-name">ShiftWell Clinics</span>
    </div>
  </section>

  <section class="card card-front" aria-label="Card front">
    <div class="brand">
      <span class="brand-dot"></span>
      <span class="brand-name">ShiftWell<br>Clinics</span>
    </div>
    <div class="divider"></div>
    <div class="person">
      <h1 class="person-name">Daniel Reyes</h1>
      <p class="person-title">Executive Manager</p>
      <ul class="contacts">
        <li>
          <span class="icon"><svg viewBox="0 0 10 10"><path d="M2 1.5 L3.6 1.5 L4.2 3.3 L3.2 4 Q4 5.9 6 6.8 L6.7 5.8 L8.5 6.4 L8.5 8 Q4.5 8.3 2 5 Q1.4 3.4 2 1.5Z" fill="#fff"/></svg></span>
          555-014-278
        </li>
        <li>
          <span class="icon"><svg viewBox="0 0 10 10"><rect x="1.5" y="2.5" width="7" height="5" fill="none" stroke="#fff" stroke-width="1"/><path d="M1.5 2.5 L5 5.3 L8.5 2.5" fill="none" stroke="#fff" stroke-width="1"/></svg></span>
          info@shiftwellclinics.com
        </li>
        <li>
          <span class="icon"><svg viewBox="0 0 10 10"><path d="M5 1.2 Q7.8 1.2 7.8 4 Q7.8 6 5 8.8 Q2.2 6 2.2 4 Q2.2 1.2 5 1.2Z" fill="#fff"/><circle cx="5" cy="4" r="1.1" fill="#f2a93b"/></svg></span>
          12 Harbor Road, Dockside, box 40210
        </li>
      </ul>
    </div>
  </section>

</main>
</body>
</html>
```